Word Page Templates x 5

1 x Letterhead Template with Header and Footer able to be printed to paper and pdf with non blurry resolution
- File attached looks ok on computer screen but does not print the same
- We are wanting it to print like it looks on the screen
- We are wanting it to print not fuzzy in resolution
- We are wanting the banner to be on the absolute edge of the page like it is on the computer screen
- We are needing to print this to paper and pdf with perfect resolution and colour

Please can someone help us!!

I have provided the logo files in our posession. If better resolutions are required please let us know.

We are also wanting 4 simple page templates to be setup in Landscape and Portrait orientation as well once we are happy with the letterhead that is provided samples have been provided
Updates

Hi all I have the vector files available now along with a Colour profile

Requirements
Must have
• Clear when printed on A4 Paper
Should not have
• Blurry images, Colour must be correct (same as Logo) - Please reference our website if need be ..... vornal.com.au

```html
<!DOCTYPE html>
<html lang="en">
<head>
<meta charset="utf-8">
<title>Vornal Pavement Services – Letterhead</title>
<link href="https://fonts.googleapis.com/css2?family=Carlito:wght@400;700&family=Open+Sans:wght@600;800&family=Questrial&display=swap" rel="stylesheet">
<style>
  :root {
    --green: #1e7a3c;
    --navy: #213a7e;
    --purple: #3d3a78;
    --grey: #6b6b6b;
    --ink: #1b1b1b;
    --paper: #ffffff;
  }
  * { margin: 0; padding: 0; box-sizing: border-box; }
  html, body { width: 848px; height: 1200px; overflow: hidden; background: var(--paper); }
  .page { position: relative; width: 848px; height: 1200px; font-family: "Carlito", sans-serif; }

  .edge-band { position: absolute; left: 0; width: 848px; height: 17px;
    background: linear-gradient(90deg, var(--green), var(--navy) 55%, var(--purple)); }
  .edge-band.top { top: 0; }
  .edge-band.bottom { bottom: 0; }

  .brand { position: absolute; font-family: "Open Sans", sans-serif; font-weight: 800; color: var(--navy); line-height: 1; }
  .brand-header { left: 29px; top: 64px; font-size: 62px; letter-spacing: 1px; }
  .brand-tag { position: absolute; font-family: "Open Sans", sans-serif; font-weight: 600; color: var(--grey); letter-spacing: 1px; }
  .brand-tag.header { left: 117px; top: 134px; font-size: 16px; }

  .company-contact { position: absolute; left: 581px; top: 67px; font-family: "Open Sans", sans-serif; font-weight: 600; font-size: 12.5px; color: var(--navy); list-style: none; }
  .company-contact li { height: 22px; }
  .company-contact b { display: inline-block; width: 25px; color: var(--green); }

  .recipient { position: absolute; left: 29px; top: 251px; font-family: "Questrial", sans-serif; color: var(--grey); }
  .recipient .name { color: var(--green); font-size: 16.5px; font-weight: 700; }
  .recipient .role { font-size: 13px; margin-top: 2px; font-weight: 600; }
  .recipient .line { margin-top: 4px; }
  .recipient .line b { color: var(--navy); font-weight: 400; }
  .recipient .addr { font-size: 14px; margin-top: 8px; }
  .recipient .small { font-size: 11px; }

  .date { position: absolute; right: 57px; top: 340px; font-family: "Questrial", sans-serif; font-size: 15px; color: var(--grey); }
  .date b { color: var(--navy); font-family: "Open Sans", sans-serif; font-weight: 600; font-size: 14px; }

  .letter-body { position: absolute; left: 29px; top: 407px; width: 780px; font-size: 14.6px; line-height: 18.5px; color: var(--grey); }
  .letter-body p { margin-bottom: 18.5px; }
  .letter-body p.emphasis { color: var(--ink); }

  .signature { position: absolute; left: 36px; top: 806px; width: 180px; height: 48px; background: linear-gradient(90deg, #eef6f0, #f7fbf8); border-radius: 4px; }
  .sign-rule { position: absolute; left: 36px; top: 865px; width: 220px; border-top: 1.5px dashed #333; }
  .signer { position: absolute; left: 46px; top: 878px; }
  .signer .name { font-family: "Open Sans", sans-serif; font-weight: 600; font-size: 20px; letter-spacing: 2px; color: var(--ink); }
  .signer .role { font-family: "Open Sans", sans-serif; font-weight: 600; font-size: 15.5px; color: var(--green); margin-top: 2px; }

  .rule { position: absolute; height: 5px; }
  .rule.navy { left: 29px; top: 1009px; width: 466px; background: var(--navy); }
  .rule.green { left: 611px; top: 1008px; width: 210px; background: var(--green); }

  .affiliations-title { position: absolute; left: 29px; top: 1029px; font-family: "Open Sans", sans-serif; font-weight: 600; font-size: 14px; letter-spacing: 1.3px; color: var(--navy); }
  .affiliates { position: absolute; left: 29px; top: 1066px; display: flex; align-items: center; gap: 14px; }
  .affiliate-badge { background: #e4e8f0; border-radius: 6px; }

  .brand-footer { left: 616px; top: 1084px; font-size: 44px; }
  .brand-tag.footer { left: 677px; top: 1130px; font-size: 12px; }
</style>
</head>
<body>
<div class="page">
  <div class="edge-band top"></div>

  <header>
    <div class="brand brand-header">VORNAL</div>
    <div class="brand-tag header">PAVEMENT SERVICES</div>
    <ul class="company-contact">
      <li><b>A:</b> PO Box 2318, Carvella Qld 4199</li>
      <li><b>P:</b> 07 5500 0142</li>
      <li><b>E:</b> admin@vornal.com.au</li>
      <li><b>W:</b> www.vornal.com.au</li>
    </ul>
  </header>

  <section class="recipient">
    <div class="name">Liam Carter</div>
    <div class="role">Chief Executive Officer</div>
    <div class="line addr"><b>A:</b> 48 Harlow Street, CA, USA 123456</div>
    <div class="line small"><b>P:</b> +91 80000 41276, +91 10000 53918</div>
    <div class="line small"><b>M:</b> info@northwaystudio.com, www.northwaystudio.com</div>
  </section>
  <div class="date"><b>Date:</b> 24-03-2018</div>

  <main class="letter-body">
    <p>Lorem ipsum dolor sit amet, consectetur adipiscing elit. Pellentesque dictum, ante non ullamcorp er convallis, nunc quam blandit metus, ac mollis eros felis a orci. Donec congue, mauris ut pulvinar lobortis, dolor massa feugiat nisi, at tincidunt metus leo vel elit.</p>
    <p>Nulla egestas vulputate risus, ut vestibulum diam commodo id. Mauris ornare libero eu erat portt itor ultrices. Proin sed lectus scelerisque ligula bibendum sagittis ac nec leo. Donec ac accumsan diam, et lobortis mauris. Nulla congue volutpat nisl ac lobortis.</p>
    <p class="emphasis">Nulla congue volutpat nisl ac lobortis. Integer dignissim interdum libero, quis feugiat velit pretium at. Phasellus sit amet libero rutrum, feugiat odio et, tempus purus. Cras ultricies, leo at fringilla solli cit udin, leo sapien placerat enim, a rutrum lorem enim ut tortor. Phasellus magna ante, cong ue maximus egestas sit amet, venenatis scelerisque felis.</p>
    <p>Nulla congue volutpat nisl ac lobortis. Integer dignissim interdum libero, quis feugiat velit pretium at. Phasellus sit amet libero rutrum, feugiat odio et, tempus purus. Cras ultricies, leo at fringilla solli cit udin, leo sapien placerat enim, a rutrum lorem enim ut tortor. Phasellus magna ante, cong ue maximus egestas sit amet, venenatis scelerisque felis</p>
  </main>

  <div class="signature" role="img" aria-label="Handwritten signature of Liam Carter"></div>
  <div class="sign-rule"></div>
  <div class="signer">
    <div class="name">Liam Carter</div>
    <div class="role">Director</div>
  </div>

  <footer>
    <div class="rule navy"></div>
    <div class="rule green"></div>
    <div class="affiliations-title">VORNAL PAVEMENT SERVICES ARE PROUDLY AFFILIATED WITH</div>
    <div class="affiliates">
      <div class="affiliate-badge" style="width:176px;height:66px"></div>
      <div class="affiliate-badge" style="width:100px;height:66px"></div>
      <div class="affiliate-badge" style="width:70px;height:74px"></div>
      <div class="affiliate-badge" style="width:62px;height:60px"></div>
    </div>
    <div class="brand brand-footer">VORNAL</div>
    <div class="brand-tag footer">PAVEMENT SERVICES</div>
  </footer>

  <div class="edge-band bottom"></div>
</div>
</body>
</html>
```